Tidewell Recovery Business Card Design

Professional and clean design. The design colors should flow with the logo. Two-sided card with the website on the back which is:

www.TidewellRecovery.example.

"Specializing in Water Damage Restoration"

On the front I need the name, email, phone, and logo.

Name: Dorian Vashti
Email: Dorian@TidewellRecovery.example
Phone: 555-318-2046 for now

I only have the Preview and Thumbnail right now but should have the source files uploaded within a day or two.

Target Market(s)

Flood victims, home owners with water damage from busted pipes etc...

Industry/Entity Type

Business

Contact Information for Business Card

Name: Dorian Vashti

Font styles to use
Serif
Sans Serif

```html
<!DOCTYPE html>
<html lang="en">
<head>
<meta charset="utf-8">
<title>Tidewell Recovery Business Card</title>
<link rel="stylesheet" href="https://fonts.googleapis.com/css2?family=Cinzel:wght@600&family=Open+Sans:wght@400;700&display=swap">
<style>
  :root {
    --brand-blue: #2596d8;
    --brand-sky: #55c1ee;
    --card-white: #ffffff;
    --page-bg: #e9edf0;
    --text-blue: #2590d2;
  }
  * { box-sizing: border-box; margin: 0; padding: 0; }
  html, body { width: 1200px; height: 900px; overflow: hidden; }
  body {
    background: var(--page-bg);
    font-family: "Open Sans", Arial, sans-serif;
    position: relative;
  }
  .card {
    position: absolute;
    width: 640px;
    height: 366px;
    background: var(--card-white);
    border-radius: 22px;
    overflow: hidden;
    box-shadow: 0 10px 30px rgba(0,0,0,0.15);
  }
  .card-back { left: 280px; top: 50px; }
  .card-front { left: 280px; top: 484px; }
  .wave { position: absolute; left: 0; top: 0; width: 100%; height: 100%; }

  /* back side */
  .back-mark {
    position: absolute;
    left: 0; right: 0; top: 50px;
    display: flex; flex-direction: column; align-items: center; gap: 12px;
  }
  .back-mark .mark-circle {
    width: 110px; height: 110px; border-radius: 50%;
    background: var(--brand-sky);
  }
  .back-mark .mark-name {
    font-family: "Cinzel", Georgia, serif;
    font-weight: 600;
    font-size: 28px;
    color: var(--brand-blue);
    letter-spacing: 1px;
  }
  .back-website {
    position: absolute;
    left: 34px; bottom: 20px;
    color: var(--card-white);
    font-size: 17px;
    letter-spacing: 0.3px;
  }

  /* front side */
  .front-brand {
    position: absolute;
    left: 24px; top: 96px;
    width: 250px;
    display: flex; flex-direction: column; align-items: center; gap: 8px;
  }
  .front-brand .mark-circle {
    width: 60px; height: 60px; border-radius: 50%;
    background: var(--brand-sky);
  }
  .front-brand .mark-name {
    font-family: "Cinzel", Georgia, serif;
    font-weight: 600;
    font-size: 24px;
    color: var(--brand-blue);
    text-align: center;
    line-height: 1.2;
  }
  .divider {
    position: absolute;
    left: 290px; top: 80px;
    width: 2px; height: 112px;
    background: var(--brand-blue);
  }
  .contact {
    position: absolute;
    left: 308px; top: 80px;
    color: var(--text-blue);
  }
  .contact-name {
    font-weight: 700;
    font-size: 22px;
    letter-spacing: 0.5px;
    text-transform: uppercase;
    margin-bottom: 10px;
    line-height: 1.3;
  }
  .contact-list { list-style: none; font-size: 14px; line-height: 1.5; }
  .contact-list li { display: flex; align-items: center; gap: 8px; }
  .contact-list svg { width: 12px; height: 12px; flex: none; }
</style>
</head>
<body>

<section class="card card-back" aria-label="Card back">
  <svg class="wave" viewBox="0 0 640 366" preserveAspectRatio="none" aria-hidden="true">
    <path d="M0 318 C200 300 420 270 640 228 L640 244 C420 288 200 318 0 334 Z" fill="var(--brand-sky)"/>
    <path d="M0 328 C210 312 430 282 640 240 L640 366 L0 366 Z" fill="var(--brand-blue)"/>
  </svg>
  <div class="back-mark">
    <div class="mark-circle"></div>
    <div class="mark-name">Tidewell Recovery</div>
  </div>
  <p class="back-website">www.TidewellRecovery.example</p>
</section>

<section class="card card-front" aria-label="Card front">
  <svg class="wave" viewBox="0 0 640 366" preserveAspectRatio="none" aria-hidden="true">
    <path d="M0 332 C240 332 440 270 640 190 L640 204 C440 285 240 344 0 344 Z" fill="var(--brand-sky)"/>
    <path d="M0 347 C250 348 450 286 640 207 L640 366 L0 366 Z" fill="var(--brand-blue)"/>
    <path d="M0 356 C260 358 470 305 640 240 L640 366 L0 366 Z" fill="var(--brand-sky)"/>
  </svg>
  <div class="front-brand">
    <div class="mark-circle"></div>
    <div class="mark-name">Tidewell Recovery</div>
  </div>
  <div class="divider"></div>
  <div class="contact">
    <h1 class="contact-name">Dorian Vashti</h1>
    <ul class="contact-list">
      <li>
        <svg viewBox="0 0 24 24" aria-hidden="true"><path d="M6.6 10.8a15 15 0 0 0 6.6 6.6l2.2-2.2a1 1 0 0 1 1-.25 11.4 11.4 0 0 0 3.6.57 1 1 0 0 1 1 1V20a1 1 0 0 1-1 1A17 17 0 0 1 3 4a1 1 0 0 1 1-1h3.5a1 1 0 0 1 1 1c0 1.25.2 2.45.57 3.6a1 1 0 0 1-.25 1z" fill="currentColor"/></svg>
        555-318-2046
      </li>
      <li>
        <svg viewBox="0 0 24 24" aria-hidden="true"><rect x="2" y="5" width="20" height="14" rx="2" fill="none" stroke="currentColor" stroke-width="2"/><path d="M3 6l9 7 9-7" fill="none" stroke="currentColor" stroke-width="2"/></svg>
        Dorian@TidewellRecovery.example
      </li>
      <li>
        <svg viewBox="0 0 24 24" aria-hidden="true"><circle cx="12" cy="12" r="9" fill="none" stroke="currentColor" stroke-width="2"/><path d="M3 12h18M12 3c3 3 3 15 0 18M12 3c-3 3-3 15 0 18" fill="none" stroke="currentColor" stroke-width="1.6"/></svg>
        www.TidewellRecovery.example
      </li>
    </ul>
  </div>
</section>

</body>
</html>
```